Web Design Project

Looking for a simple, yet creative, small company website that can grow with me. The company name is Dorvel Solutions and the first products will be branded as TorraWarm warmers.

The first product I am selling are small reusable sodium acetate warming pads directed to two markets. 1) outdoor sporting/hunting activities and 2) spa/heat therapy. Three different sizes of warmers are currently availaible.

One differentiating aspect of our product is a custom designed neoprene insulating sleeve into which the warmer fits so that it stays warmer longer.

Looking for a website that is simple, easy to navigate and fun.

I would like to be able to sell items directly from website and direct to Quillmart as well.

I have a logo to base your ideas on.

Pictures of the first three products. Please incorporate.

Requirements
Must have
• selling cart
contact page
how they work
Nice to have
• product video, may be added later

```html
<!DOCTYPE html>
<html lang="en">
<head>
<meta charset="utf-8">
<title>TorraWarm – Dorvel Solutions</title>
<link rel="stylesheet" href="https://fonts.googleapis.com/css2?family=Roboto+Condensed:wght@300;400;700&family=Roboto:wght@400;500&display=swap">
<style>
:root{
  --purple:#6a1f86;
  --purple-dark:#4b1060;
  --ink:#222;
  --text:#444;
  --muted:#666;
  --line:#d9d9d9;
  --hero:#eef0f2;
  --foot-top:#4a4a4a;
  --foot-bot:#1d1d1d;
  --btn:#5a5a5a;
}
*{box-sizing:border-box;margin:0;padding:0}
html,body{width:1072px;height:1200px;overflow:hidden;background:#fff;font-family:"Roboto",Arial,sans-serif;color:var(--text)}
.page{position:relative;width:1072px;height:1200px}
.abs{position:absolute}

/* header */
.brand{left:77px;top:6px;display:flex;align-items:center;gap:10px}
.brand-mark{width:60px;height:60px;background:var(--purple);border-radius:8px}
.brand-name{font-family:"Roboto Condensed",sans-serif;font-weight:700;font-size:38px;color:var(--ink);letter-spacing:.5px}
.cart{left:686px;top:17px;font-size:13px;color:var(--purple);display:flex;align-items:center;gap:6px}
.search{left:777px;top:15px;width:218px;height:22px;border:1px solid #ccc;display:flex}
.search span{flex:1;font-size:12px;color:#aaa;padding:3px 7px}
.search i{width:22px;background:#9a7cb8;border-left:1px solid #7d5a9e}
.nav{left:395px;top:53px;display:flex;gap:0;font-size:12px;font-weight:500;color:var(--ink)}
.nav a{text-decoration:none;color:inherit;position:relative}
.nav .sep{margin:0 14px}
.nav a.active::after{content:"";position:absolute;left:0;right:0;bottom:-13px;height:5px;background:var(--purple)}
.rule{left:0;top:81px;width:1072px;border-top:1px dotted #ccc}

/* hero */
.hero{left:0;top:85px;width:1072px;height:380px;background:linear-gradient(90deg,#f2f3f4 0%,#eceef0 45%,#e3e5e8 100%)}
.hero-photo{left:470px;top:85px;width:440px;height:380px;background:radial-gradient(ellipse at 50% 40%,#e7d2c4 0%,#d8dde3 55%,rgba(230,232,235,0) 80%)}
.hero-copy{left:130px;top:176px;width:420px;font-family:"Roboto Condensed",sans-serif;font-weight:300;color:var(--ink)}
.hero-copy h1{font-weight:300;font-size:21px;line-height:27px}
.hero-copy ul{list-style:none;margin-top:12px;font-size:18px;line-height:27px}
.hero-copy li::before{content:"›";font-weight:700;margin-right:8px}
.read-more{left:131px;top:305px;width:172px;height:45px;background:linear-gradient(#7a2b98,var(--purple-dark));border:1px solid #3b0a4c;color:#fff;font-family:"Roboto Condensed",sans-serif;font-weight:700;font-size:26px;display:flex;align-items:center;justify-content:center;gap:8px}
.read-more b{width:22px;height:22px;border-radius:50%;background:#fff;color:var(--purple);font-size:14px;display:flex;align-items:center;justify-content:center}
.arrow{top:256px;width:36px;height:36px;background:#d4d6d8;color:#666;font-size:22px;display:flex;align-items:center;justify-content:center}
.pager{left:479px;top:448px;width:143px;height:32px;background:#f3f3f3;border-radius:5px;display:flex;align-items:center;justify-content:center;gap:5px;color:#444;font-size:16px}
.pager i{width:12px;height:12px;border-radius:50%;background:#888;border:2px solid #ccc}
.pager span{margin:0 8px}

/* cards */
.card{top:498px;width:292px;height:400px;border:1px solid var(--line);border-radius:12px;background:#fff;box-shadow:0 8px 12px -8px rgba(0,0,0,.15)}
.card h2{height:45px;background:linear-gradient(#7d2fa0,var(--purple-dark));color:#fff;font-family:"Roboto Condensed",sans-serif;font-weight:700;font-size:22px;padding:9px 26px;border-radius:12px 12px 0 0}
.card .media{position:absolute;left:16px;top:60px;width:257px;height:105px}
.card .body{position:absolute;left:16px;top:182px;width:258px;font-size:12.5px;line-height:16px;text-align:justify}
.card .body p+p{margin-top:14px}
.card ul{list-style:none;margin-top:22px;line-height:22px}
.card li::before{content:"›";font-weight:700;margin-right:8px}
.more{position:absolute;right:22px;top:345px;width:60px;height:29px;border-radius:7px;background:linear-gradient(#777,#4d4d4d);color:#fff;font-family:"Roboto Condensed",sans-serif;font-size:17px;display:flex;align-items:center;justify-content:center}
.logo-box{border:1px solid #ddd;display:flex;align-items:center;justify-content:center;gap:10px}
.logo-box .brand-mark{width:52px;height:52px}
.logo-box .brand-name{font-size:34px}
.player{position:absolute;left:16px;top:60px;width:258px;height:160px}
.player .screen{width:258px;height:145px;background:linear-gradient(135deg,#dfe4ea,#b9c1ca 60%,#8f9aa6)}
.player .play{position:absolute;left:101px;top:45px;width:56px;height:56px;border-radius:50%;background:#333;border:3px solid #ccc;display:flex;align-items:center;justify-content:center}
.player .bar{height:15px;background:#e6e6e6;border:1px solid #ccc;position:relative}
.player .bar i{position:absolute;left:22px;right:110px;top:6px;height:2px;background:#999}

/* footer */
.footer{left:0;top:933px;width:1072px;height:267px;background:linear-gradient(var(--foot-top),var(--foot-bot));color:#fff}
.fcol{top:943px;height:208px;border-right:1px solid #666}
.ftitle{font-size:23px;font-weight:400}
.phone{font-size:25px;margin-top:6px}
.field{position:absolute;background:#fff;color:#333;font-size:11px;padding:7px 9px}
.submit{left:337px;top:1119px;width:60px;height:28px;border-radius:6px;background:linear-gradient(#3a3a3a,#0f0f0f);font-family:"Roboto Condensed",sans-serif;font-size:17px;display:flex;align-items:center;justify-content:center}
.links{list-style:none;font-size:11.5px;line-height:18.8px;margin-top:10px;margin-left:2px}
.links li::before{content:"›";font-weight:700;margin-right:8px}
.social{display:flex;gap:14px;margin-top:14px}
.social i{width:35px;height:35px;background:#6a6a6a;border:1px solid #888}
.copy{left:78px;top:1166px;width:915px;height:34px;background:#5b5b5b;font-size:11px;color:#eee;display:flex;align-items:center;justify-content:center}
</style>
</head>
<body>
<div class="page">
  <header>
    <div class="abs brand"><span class="brand-mark"></span><span class="brand-name">TorraWarm</span></div>
    <div class="abs cart">
      <svg width="18" height="14" viewBox="0 0 18 14"><path d="M1 2h3l2 7h9l2-6H5" fill="none" stroke="#6a1f86" stroke-width="1.6"/><circle cx="7" cy="12" r="1.3" fill="#6a1f86"/><circle cx="14" cy="12" r="1.3" fill="#6a1f86"/></svg>
      View Cart
    </div>
    <div class="abs search"><span>Type your search here...</span><i></i></div>
    <nav class="abs nav">
      <a class="active">HOME</a><span class="sep">/</span>
      <a>ABOUT US</a><span class="sep">/</span>
      <a>SERVICES</a><span class="sep">/</span>
      <a>GALLERY</a><span class="sep">/</span>
      <a>BLOG</a><span class="sep">/</span>
      <a>TESTIMONIALS</a><span class="sep">/</span>
      <a>CONTACT US</a>
    </nav>
    <div class="abs rule"></div>
  </header>

  <section>
    <div class="abs hero"></div>
    <div class="abs hero-photo" role="img" aria-label="Photo of a smiling woman in a light suit"></div>
    <div class="abs hero-copy">
      <h1>We create warmers. We sell small reusable sodium acetate warming pads directed to two markets.</h1>
      <ul><li>Outdoor sporting/hunting activities</li><li>Spa/heat therapy.</li></ul>
    </div>
    <div class="abs read-more">Read More <b>▶</b></div>
    <div class="abs arrow" style="left:20px">‹</div>
    <div class="abs arrow" style="left:1014px">›</div>
    <div class="abs pager"><span>‹</span><i></i><i></i><i></i><i></i><span>›</span></div>
  </section>

  <section>
    <article class="abs card" style="left:75px">
      <h2>About Us</h2>
      <div class="media" style="background:linear-gradient(90deg,#d9d4cf,#9a958f 40%,#e8e6e3 60%,#a8a09a)" role="img" aria-label="Photo of a business team"></div>
      <div class="body">
        <p>We create warmers. We sell small reusable sodium acetate warming pads directed to two markets. Three different sizes of warmers are currently available.</p>
        <ul><li>Outdoor sporting/hunting activities</li><li>Spa/heat therapy.</li></ul>
      </div>
      <div class="more">More</div>
    </article>

    <article class="abs card" style="left:389px">
      <h2>Our Products</h2>
      <div class="media logo-box"><span class="brand-mark"></span><span class="brand-name">TorraWarm</span></div>
      <div class="body">
        <p>Sed ut perspiciatis unde omnis iste natus error sit voluptatem accusantium doloremque laudantium, totam rem aperiam.</p>
        <p>Nemo enim ipsam voluptatem quia voluptas sit aspernatur aut odit aut fugit, sed quia consequuntur magni dolores eos qui ratione voluptatem sequi nesciunt.</p>
      </div>
      <div class="more">More</div>
    </article>

    <article class="abs card" style="left:702px">
      <h2>How it Works</h2>
      <div class="player">
        <div class="screen" role="img" aria-label="Video still of a team meeting"></div>
        <div class="play"><svg width="20" height="22"><path d="M3 1l16 10L3 21z" fill="#fff"/></svg></div>
        <div class="bar"><i></i></div>
      </div>
      <div class="body" style="top:236px">
        <p>Sed ut perspiciatis unde omnis iste natus error sit voluptatem accusantium doloremque laudantium, totam rem aperiam.</p>
        <p>Sed ut perspiciatis unde omnis iste natus error sit voluptatem accusantium doloremque laudantium, totam rem aperiam.</p>
      </div>
      <div class="more">More</div>
    </article>
  </section>

  <footer>
    <div class="abs footer"></div>
    <div class="abs fcol" style="left:78px;width:236px;padding-top:18px">
      <div class="ftitle" style="color:#fff">Call Sales</div>
      <div class="phone" style="color:#fff">123 456 7890</div>
    </div>
    <div class="abs fcol" style="left:314px;width:250px;padding:18px 0 0 23px">
      <div class="ftitle" style="color:#fff">Contact Information</div>
    </div>
    <div class="abs field" style="left:337px;top:1002px;width:215px;height:27px">Name</div>
    <div class="abs field" style="left:337px;top:1040px;width:215px;height:66px">Message</div>
    <div class="abs submit" style="color:#fff">Submit</div>
    <div class="abs fcol" style="left:564px;width:197px;padding:18px 0 0 23px;color:#fff">
      <div class="ftitle">Quick Links</div>
      <ul class="links"><li>Home</li><li>About Us</li><li>Services</li><li>Gallery</li><li>Blog</li><li>Testimonials</li><li>Contact Us</li></ul>
    </div>
    <div class="abs" style="left:785px;top:961px;color:#fff">
      <div class="ftitle">Follow us on</div>
      <div class="social"><i></i><i></i><i></i><i></i></div>
    </div>
    <div class="abs copy">Copyrights © 2012. All Rights Reserved.</div>
  </footer>
</div>
</body>
</html>
```